Redesign of Medical App for Patients

• The Designer’s task is to provide a new fully-responsive design for our apps, and then code it using only basic html and CSS.
• Your design will be incorporated into our existing REACT native app.

Target Market(s)

Medical Patients

Industry/Entity Type

Medical

Coding

Coded - Design and coding required

Number of Pages Required

5+ page

Requirements
Must have
• Short list candidates will receive detailed briefing
Nice to have
• detailed briefing contains some of our ideas.

```html
<!DOCTYPE html>
<html lang="en">
<head>
<meta charset="utf-8">
<title>CareGuide – Patient App Screens</title>
<link href="https://fonts.googleapis.com/css2?family=Poppins:wght@400;500;600;700&display=swap" rel="stylesheet">
<style>
:root{
  --blue:#0b8ec9;
  --blue-light:#1aa9e6;
  --orange:#f4742b;
  --ink:#333a3f;
  --muted:#8a9096;
  --card:#f3f4f5;
  --board:#e8e9ea;
  --white:#ffffff;
}
*{box-sizing:border-box;margin:0;padding:0}
html,body{width:1200px;height:3947px;overflow:hidden}
body{background:var(--board);font-family:'Poppins',sans-serif;color:var(--ink);position:relative}
.deco{position:absolute;border-radius:50%;background:var(--orange)}
.deco-top{left:770px;top:250px;width:800px;height:680px}
.deco-bottom{left:-110px;top:3240px;width:990px;height:990px}
.brand{position:absolute;top:84px;left:250px;display:flex;align-items:center;gap:40px}
.brand-dot{width:132px;height:132px;border-radius:50%;background:var(--blue)}
.brand-name{font-size:78px;font-weight:500;color:var(--ink);letter-spacing:1px}
.screen{position:absolute;width:334px;height:728px;border-radius:34px;overflow:hidden;background:var(--white);box-shadow:0 20px 40px rgba(60,80,110,.18)}
.col-l{left:158px}.col-r{left:624px}
.head{position:absolute;inset:0 0 auto 0;height:130px;background:var(--blue)}
.head-title{position:absolute;top:52px;left:0;right:0;text-align:center;color:var(--white);font-size:20px;font-weight:600}
.head-icon{position:absolute;top:58px;left:20px;width:20px;height:16px}
.body{position:absolute;top:104px;left:0;right:0;bottom:0;background:var(--white);border-radius:24px 24px 0 0}
.tabbar{position:absolute;left:0;right:0;bottom:0;height:58px;background:var(--white);border-top:1px solid #eee;display:flex;justify-content:space-around;align-items:center;padding:0 14px}
.tab{display:flex;flex-direction:column;align-items:center;gap:3px;font-size:7px;font-weight:600;color:var(--ink);position:relative;width:50px}
.tab svg{width:18px;height:16px;stroke:#8a9096;fill:none;stroke-width:1.3}
.tab.active{color:var(--orange)}
.tab.active svg{stroke:var(--orange)}
.tab.active::before{content:"";position:absolute;top:-12px;width:18px;height:3px;background:var(--orange)}
.list{position:absolute;left:18px;right:18px;display:flex;flex-direction:column}
.row{background:var(--card);border-radius:6px;display:flex;align-items:center;padding:0 12px;position:relative}
.row-title{font-size:12px;font-weight:600}
.row-sub{font-size:8px;color:var(--muted);margin-top:2px}
.chev{position:absolute;right:12px;width:16px;height:16px;border-radius:50%;background:var(--white);font-size:9px;color:var(--muted);display:flex;align-items:center;justify-content:center}
.dot-go{position:absolute;right:16px;width:20px;height:20px;border-radius:50%;background:var(--orange)}
.toc-icon{width:40px;height:36px;margin-right:12px;stroke:var(--blue);fill:none;stroke-width:1.5}
.team-card{background:var(--card);border-radius:6px;height:122px;position:relative}
.avatar{position:absolute;left:18px;top:18px;width:86px;height:86px;border-radius:50%}
.team-info{position:absolute;left:118px;top:18px;font-size:8px}
.team-info h3{font-size:14px;font-weight:600;margin-bottom:8px}
.team-info p{margin-bottom:6px;line-height:1.3}
.team-info b{font-weight:600}
.team-info .ic{color:var(--orange);margin-right:4px}
.media{position:absolute;left:18px;right:18px;height:187px;border-radius:4px}
.play{position:absolute;right:30px;bottom:-18px;width:46px;height:46px;border-radius:50%;background:var(--orange)}
.play::after{content:"";position:absolute;left:19px;top:16px;border-left:11px solid var(--white);border-top:7px solid transparent;border-bottom:7px solid transparent}
.toggle{position:absolute;right:24px;width:22px;height:10px;border:1px solid #ccc;border-radius:6px}
.toggle::before{content:"";position:absolute;left:-1px;top:-1px;width:10px;height:10px;border:1px solid #ccc;border-radius:50%;background:var(--white)}
.select{position:absolute;left:18px;right:18px;top:115px;height:34px;border-radius:17px;background:var(--blue-light);color:#d4efff;font-size:10px;display:flex;align-items:center;padding:0 22px;justify-content:space-between}
.drawer{position:absolute;top:0;left:0;bottom:0;width:181px;background:var(--white);padding:48px 16px 0 18px}
.drawer-close{width:20px;height:20px;border:1.5px solid var(--ink);border-radius:50%;display:flex;align-items:center;justify-content:center;font-size:11px;margin-bottom:12px}
.drawer-sec{background:#e8e9ea;font-size:11px;font-weight:600;padding:6px 10px;margin:0 -2px 6px}
.drawer-item{font-size:9px;line-height:17px;margin-left:-2px}
.drawer-gap{height:20px}
.shade{position:absolute;inset:0;background:rgba(40,45,50,.55)}
</style>
</head>
<body>

<div class="deco deco-top"></div>
<div class="deco deco-bottom"></div>

<div class="brand"><div class="brand-dot"></div><div class="brand-name">CAREGUIDE</div></div>

<!-- Splash -->
<section class="screen col-l" style="top:317px;background:linear-gradient(180deg,#d9eefb 0%,#ffffff 55%)">
  <div style="position:absolute;left:117px;top:248px;width:100px;height:100px;border-radius:50%;background:var(--blue)"></div>
  <div style="position:absolute;top:402px;left:0;right:0;text-align:center;font-size:34px;font-weight:500">CAREGUIDE</div>
  <div style="position:absolute;bottom:28px;left:107px;width:120px;height:4px;border-radius:2px;background:#d8d8d8"></div>
</section>

<!-- Intro -->
<section class="screen col-r" style="top:455px;background:linear-gradient(160deg,#0e8bc6,#0a9ad8 60%,#12b0ee)">
  <div style="position:absolute;left:120px;top:84px;width:94px;height:94px;border-radius:50%;background:var(--white)"></div>
  <div style="position:absolute;top:294px;width:100%;text-align:center;color:var(--white);font-size:15px;font-weight:600">The Recovery Handbook</div>
  <div style="position:absolute;top:326px;width:100%;text-align:center;color:var(--white);font-size:40px;font-weight:700;line-height:42px">Distal Radius<br>Fractures</div>
  <div style="position:absolute;top:424px;width:100%;text-align:center;color:#e4f5ff;font-size:13px;line-height:20px">Almost everything you need to know<br>before, during, and after your surgery.</div>
  <div style="position:absolute;left:15px;right:15px;top:614px;height:38px;border-radius:19px;background:var(--orange);color:var(--white);font-size:14px;font-weight:700;display:flex;align-items:center;justify-content:center">CONTINUE<span style="position:absolute;right:18px;font-weight:400">→</span></div>
</section>

<!-- Table of contents -->
<section class="screen col-l" style="top:1165px">
  <div class="head"><svg class="head-icon" viewBox="0 0 20 16" stroke="#fff" fill="none" stroke-width="1.5"><path d="M18 8H3M8 3L3 8l5 5"/></svg><div class="head-title">Table of Contents</div></div>
  <div class="body">
    <div class="list" style="top:30px;gap:6px">
      <div class="row" style="height:64px"><svg class="toc-icon" viewBox="0 0 40 36"><rect x="4" y="6" width="30" height="24" rx="2"/><path d="M10 14h18M10 20h12"/></svg><div><div class="row-title">About procedure</div><div class="row-sub">Why and how is it done</div></div><span class="chev">›</span></div>
      <div class="row" style="height:64px"><svg class="toc-icon" viewBox="0 0 40 36"><path d="M6 8v20M14 10h6v8h-6v10h6M26 10h7l-5 8h5v10h-7"/></svg><div><div class="row-title">Pre-procedure</div><div class="row-sub">How to get ready</div></div><span class="chev">›</span></div>
      <div class="row" style="height:64px"><svg class="toc-icon" viewBox="0 0 40 36"><circle cx="20" cy="18" r="13"/><path d="M20 9v9l6 4"/></svg><div><div class="row-title">Procedure</div><div class="row-sub">The day of the procedure – in the…</div></div><span class="chev">›</span></div>
      <div class="row" style="height:64px"><svg class="toc-icon" viewBox="0 0 40 36"><rect x="8" y="5" width="22" height="26" rx="2"/><path d="M13 13h12M13 19h12M13 25h8"/></svg><div><div class="row-title">Recovery</div><div class="row-sub">Expectations immediately after surgery</div></div><span class="chev">›</span></div>
      <div class="row" style="height:64px"><svg class="toc-icon" viewBox="0 0 40 36"><path d="M6 16L20 5l14 11v15H6z"/><rect x="16" y="20" width="8" height="11"/></svg><div><div class="row-title">At Home</div><div class="row-sub">How to care for yourself afterwards</div></div><span class="chev">›</span></div>
      <div class="row" style="height:64px"><svg class="toc-icon" viewBox="0 0 40 36"><rect x="7" y="5" width="26" height="22" rx="2"/><circle cx="20" cy="15" r="5"/><path d="M14 31h12"/></svg><div><div class="row-title">What to do if</div><div class="row-sub">Responding to your issues</div></div><span class="chev">›</span></div>
      <div class="row" style="height:64px"><svg class="toc-icon" viewBox="0 0 40 36"><rect x="10" y="5" width="20" height="26" rx="2"/><path d="M15 18l4 4 7-8"/></svg><div><div class="row-title">Success</div><div class="row-sub">Feedback &amp; who did this app</div></div><span class="chev">›</span></div>
    </div>
  </div>
  <nav class="tabbar">
    <div class="tab active"><svg viewBox="0 0 18 16"><path d="M2 8l7-6 7 6v7H2z"/></svg>HOME</div>
    <div class="tab"><svg viewBox="0 0 18 16"><circle cx="5" cy="5" r="2.5"/><circle cx="13" cy="5" r="2.5"/><path d="M1 15v-4h8v4M9 15v-4h8v4"/></svg>TEAM</div>
    <div class="tab"><svg viewBox="0 0 18 16"><path d="M9 3L3 8l6 5M15 3L9 8l6 5"/></svg>PREVIOUS</div>
    <div class="tab"><svg viewBox="0 0 18 16"><path d="M3 3l6 5-6 5M9 3l6 5-6 5"/></svg>NEXT</div>
    <div class="tab"><svg viewBox="0 0 18 16"><circle cx="9" cy="8" r="6"/><circle cx="9" cy="8" r="2.5"/></svg>SETTING</div>
  </nav>
</section>

<!-- Care team -->
<section class="screen col-r" style="top:1336px">
  <div class="head"><svg class="head-icon" viewBox="0 0 20 16" stroke="#fff" stroke-width="1.5"><path d="M2 3h16M2 8h12M2 13h16"/></svg><div class="head-title">Your Care Team</div></div>
  <div class="body">
    <div class="list" style="top:42px;gap:12px">
      <div class="team-card">
        <div class="avatar" role="img" aria-label="Portrait photo of the procedure physician" style="background:linear-gradient(160deg,#dfe6ec,#b9c6d1)"></div>
        <div class="team-info"><h3>Procedure Physician</h3><p><span class="ic">✆</span><b>Phone*</b><br>&nbsp;&nbsp;&nbsp;555 010 2040</p><p><span class="ic">✉</span><b>Email*</b><br>&nbsp;&nbsp;&nbsp;office@careguide.example</p></div>
      </div>
      <div class="team-card">
        <div class="avatar" role="img" aria-label="Photo of the physician's office building" style="background:linear-gradient(160deg,#e9eef2,#a8b6c2)"></div>
        <div class="team-info"><h3>Physician's Office</h3><p><span class="ic">✆</span><b>Phone*</b><br>&nbsp;&nbsp;&nbsp;555 010 3171</p><p><span class="ic">✉</span><b>Email*</b><br>&nbsp;&nbsp;&nbsp;office@careguide.example</p></div>
      </div>
      <p style="font-size:8px;text-align:center;line-height:13px;padding:14px 10px 0">If, at any time, you have questions, or the communications solutions suggested in this app do not work, please either contact the hospital, or go immediately to the Emergency Department.</p>
    </div>
  </div>
  <nav class="tabbar">
    <div class="tab"><svg viewBox="0 0 18 16"><path d="M2 8l7-6 7 6v7H2z"/></svg>HOME</div>
    <div class="tab active"><svg viewBox="0 0 18 16"><circle cx="5" cy="5" r="2.5"/><circle cx="13" cy="5" r="2.5"/><path d="M1 15v-4h8v4M9 15v-4h8v4"/></svg>TEAM</div>
    <div class="tab"><svg viewBox="0 0 18 16"><path d="M9 3L3 8l6 5M15 3L9 8l6 5"/></svg>PREVIOUS</div>
    <div class="tab"><svg viewBox="0 0 18 16"><path d="M3 3l6 5-6 5M9 3l6 5-6 5"/></svg>NEXT</div>
    <div class="tab"><svg viewBox="0 0 18 16"><circle cx="9" cy="8" r="6"/><circle cx="9" cy="8" r="2.5"/></svg>SETTING</div>
  </nav>
</section>

<!-- Hello audio -->
<section class="screen col-l" style="top:2012px">
  <div class="head"><svg class="head-icon" viewBox="0 0 20 16" stroke="#fff" stroke-width="1.5"><path d="M2 3h16M2 8h12M2 13h16"/></svg><div class="head-title">Hello (Audio)</div></div>
  <div class="body">
    <div style="position:absolute;top:36px;width:100%;text-align:center;font-size:13px;font-weight:600">A message from your Surgeon</div>
    <div class="media" style="top:75px;background:linear-gradient(135deg,#9fd3e2,#6fb6cc)" role="img" aria-label="Photo of a stethoscope and blood pressure gauge on a blue surface"><span class="play"></span></div>
    <div class="media" style="top:300px;background:linear-gradient(135deg,#a5ccd8,#7fb4c6)" role="img" aria-label="Photo of a surgeon in a white coat"><span class="play"></span></div>
  </div>
  <nav class="tabbar">
    <div class="tab"><svg viewBox="0 0 18 16"><path d="M2 8l7-6 7 6v7H2z"/></svg>HOME</div>
    <div class="tab"><svg viewBox="0 0 18 16"><circle cx="5" cy="5" r="2.5"/><circle cx="13" cy="5" r="2.5"/><path d="M1 15v-4h8v4M9 15v-4h8v4"/></svg>TEAM</div>
    <div class="tab active"><svg viewBox="0 0 18 16"><path d="M9 3L3 8l6 5M15 3L9 8l6 5"/></svg>PREVIOUS</div>
    <div class="tab"><svg viewBox="0 0 18 16"><path d="M3 3l6 5-6 5M9 3l6 5-6 5"/></svg>NEXT</div>
    <div class="tab"><svg viewBox="0 0 18 16"><circle cx="9" cy="8" r="6"/><circle cx="9" cy="8" r="2.5"/></svg>SETTING</div>
  </nav>
</section>

<!-- About procedure -->
<section class="screen col-r" style="top:2216px">
  <div class="head"><svg class="head-icon" viewBox="0 0 20 16" stroke="#fff" stroke-width="1.5"><path d="M2 3h16M2 8h12M2 13h16"/></svg><div class="head-title">About procedure</div></div>
  <div class="body">
    <div class="list" style="top:42px;gap:11px">
      <div class="row" style="height:64px;padding-left:22px"><div class="row-title" style="width:170px;line-height:16px">Is it too late to prevent gallbladder disease?</div><span class="dot-go"></span></div>
      <div class="row" style="height:64px;padding-left:22px"><div class="row-title" style="width:180px;line-height:16px">What will happen if I don't have this procedure?</div><span class="dot-go"></span></div>
      <div class="row" style="height:64px;padding-left:22px"><div class="row-title" style="width:150px;line-height:16px">Are there alternative solutions?</div><span class="dot-go"></span></div>
      <div class="row" style="height:64px;padding-left:22px"><div class="row-title" style="width:170px;line-height:16px">What are the risks of this procedure?</div><span class="dot-go"></span></div>
    </div>
  </div>
  <nav class="tabbar">
    <div class="tab"><svg viewBox="0 0 18 16"><path d="M2 8l7-6 7 6v7H2z"/></svg>HOME</div>
    <div class="tab"><svg viewBox="0 0 18 16"><circle cx="5" cy="5" r="2.5"/><circle cx="13" cy="5" r="2.5"/><path d="M1 15v-4h8v4M9 15v-4h8v4"/></svg>TEAM</div>
    <div class="tab"><svg viewBox="0 0 18 16"><path d="M9 3L3 8l6 5M15 3L9 8l6 5"/></svg>PREVIOUS</div>
    <div class="tab active"><svg viewBox="0 0 18 16"><path d="M3 3l6 5-6 5M9 3l6 5-6 5"/></svg>NEXT</div>
    <div class="tab"><svg viewBox="0 0 18 16"><circle cx="9" cy="8" r="6"/><circle cx="9" cy="8" r="2.5"/></svg>SETTING</div>
  </nav>
</section>

<!-- Settings -->
<section class="screen col-l" style="top:2873px">
  <div class="head" style="height:190px"><svg class="head-icon" viewBox="0 0 20 16" stroke="#fff" stroke-width="1.5"><path d="M2 3h16M2 8h12M2 13h16"/></svg><div class="head-title">Settings</div>
    <div style="position:absolute;top:97px;left:18px;color:#fff;font-size:10px;font-weight:600">Country</div>
    <div class="select">United States<span>⌄</span></div>
  </div>
  <div class="body" style="top:176px">
    <div class="list" style="top:12px;gap:12px">
      <div class="row" style="height:64px;padding-left:28px;background:#fff;box-shadow:0 2px 10px rgba(0,0,0,.07)"><div class="row-title">Show Introductory Pages</div><span class="toggle"></span></div>
      <div class="row" style="height:64px;padding-left:28px;background:#fff;box-shadow:0 2px 10px rgba(0,0,0,.07)"><div class="row-title">Clear Return Home Date</div><span class="toggle"></span></div>
      <div class="row" style="height:64px;padding-left:28px;background:#fff;box-shadow:0 2px 10px rgba(0,0,0,.07)"><div class="row-title">Clear History</div><span class="toggle"></span></div>
    </div>
  </div>
  <nav class="tabbar">
    <div class="tab"><svg viewBox="0 0 18 16"><path d="M2 8l7-6 7 6v7H2z"/></svg>HOME</div>
    <div class="tab"><svg viewBox="0 0 18 16"><circle cx="5" cy="5" r="2.5"/><circle cx="13" cy="5" r="2.5"/><path d="M1 15v-4h8v4M9 15v-4h8v4"/></svg>TEAM</div>
    <div class="tab"><svg viewBox="0 0 18 16"><path d="M9 3L3 8l6 5M15 3L9 8l6 5"/></svg>PREVIOUS</div>
    <div class="tab"><svg viewBox="0 0 18 16"><path d="M3 3l6 5-6 5M9 3l6 5-6 5"/></svg>NEXT</div>
    <div class="tab active"><svg viewBox="0 0 18 16"><circle cx="9" cy="8" r="6"/><circle cx="9" cy="8" r="2.5"/></svg>SETTING</div>
  </nav>
</section>

<!-- Navigation drawer over settings -->
<section class="screen col-r" style="top:3085px">
  <div class="head" style="height:190px"><div class="head-title" style="left:120px">Settings</div>
    <div class="select">United States<span>⌄</span></div>
  </div>
  <div class="body" style="top:176px">
    <div class="list" style="top:12px;gap:12px">
      <div class="row" style="height:64px;padding-left:28px;background:#fff"><div class="row-title">Show Introductory Pages</div><span class="toggle"></span></div>
      <div class="row" style="height:64px;padding-left:28px;background:#fff"><div class="row-title">Clear Return Home Date</div><span class="toggle"></span></div>
      <div class="row" style="height:64px;padding-left:28px;background:#fff"><div class="row-title">Clear History</div><span class="toggle"></span></div>
    </div>
  </div>
  <nav class="tabbar">
    <div class="tab"><svg viewBox="0 0 18 16"><path d="M2 8l7-6 7 6v7H2z"/></svg>HOME</div>
    <div class="tab"><svg viewBox="0 0 18 16"><circle cx="5" cy="5" r="2.5"/><circle cx="13" cy="5" r="2.5"/><path d="M1 15v-4h8v4M9 15v-4h8v4"/></svg>TEAM</div>
    <div class="tab"><svg viewBox="0 0 18 16"><path d="M9 3L3 8l6 5M15 3L9 8l6 5"/></svg>PREVIOUS</div>
    <div class="tab"><svg viewBox="0 0 18 16"><path d="M3 3l6 5-6 5M9 3l6 5-6 5"/></svg>NEXT</div>
    <div class="tab active"><svg viewBox="0 0 18 16"><circle cx="9" cy="8" r="6"/><circle cx="9" cy="8" r="2.5"/></svg>SETTING</div>
  </nav>
  <div class="shade"></div>
  <aside class="drawer">
    <div class="drawer-close">✕</div>
    <div class="drawer-sec">Introduction</div>
    <div class="drawer-item">Title Page<br>Message to Our Patients<br>Hello (audio)</div>
    <div class="drawer-gap"></div>
    <div class="drawer-sec">Table of Contents</div>
    <div class="drawer-item">About procedure<br>Pre-procedure<br>Procedure<br>Recovery<br>At Home<br>What to do if<br>Success</div>
    <div class="drawer-gap"></div>
    <div class="drawer-sec">Other</div>
    <div class="drawer-item">Share</div>
  </aside>
</section>

</body>
</html>
```